Business card for a "family office" company

Please provide professional looking business card designs, incorporating the attached logo and below details. Harrowmere Holdings Pty Ltd is a family office / financial investment company. We are looking for a modern, professional and contemporary card design.

Industry/Entity Type

Finance

Contact Information for Business Card

Name: Dean Mollick
Title: Director
Company: Harrowmere Holdings Pty Ltd
Email: harrowdean@quillnet.example
Mobile: 0462 735 418
Address: 4/312 Barnaby Parade, Halvercombe QX 7734, Australia

Requirements
Must have
• All details above and the logo. logo only on back side. incorporate colours of logo
Nice to have
• up to you
Should not have
• ?

```html
<!DOCTYPE html>
<html lang="en">
<head>
<meta charset="utf-8">
<title>Harrowmere Holdings – Business Card</title>
<link rel="stylesheet" href="https://fonts.googleapis.com/css2?family=Open+Sans:wght@400;600;700&display=swap">
<style>
  :root {
    --navy: #27235e;
    --white: #ffffff;
    --stage: #ececec;
    --divider: #8a88a8;
  }
  * { box-sizing: border-box; margin: 0; padding: 0; }
  html, body {
    width: 1200px;
    height: 533px;
    overflow: hidden;
    background: var(--stage);
    font-family: "Open Sans", Arial, sans-serif;
  }
  .stage { position: relative; width: 1200px; height: 533px; }
  .card {
    position: absolute;
    top: 85px;
    width: 536px;
    height: 306px;
    box-shadow: 0 2px 8px rgba(0,0,0,0.12);
  }
  .card--front { left: 61px; background: var(--white); color: var(--navy); }
  .card--back { left: 623px; background: var(--navy); color: var(--white); }

  .edge-band { position: absolute; left: 0; top: 0; }

  .front-brand {
    position: absolute;
    left: 36px;
    top: 128px;
    width: 180px;
    display: flex;
    align-items: center;
    justify-content: center;
    gap: 7px;
    font-weight: 700;
    font-size: 13px;
    letter-spacing: 0.06em;
    text-transform: uppercase;
    color: var(--navy);
    text-align: center;
    line-height: 1.25;
  }
  .brand-mark { width: 10px; height: 10px; background: currentColor; flex: none; }

  .divider {
    position: absolute;
    left: 259px;
    top: 32px;
    width: 1.5px;
    height: 222px;
    background: var(--divider);
  }

  .person { position: absolute; left: 287px; top: 47px; }
  .person-name { font-weight: 700; font-size: 11px; letter-spacing: 0.03em; text-transform: uppercase; }
  .person-title { font-size: 8px; text-transform: uppercase; margin-top: 2px; }

  .contact-list { position: absolute; left: 287px; top: 104px; font-size: 8.5px; text-transform: uppercase; }
  .contact-row { display: flex; margin-bottom: 6px; line-height: 18px; }
  .contact-label { width: 42px; flex: none; }
  .contact-value { line-height: 18px; }

  .company-line {
    position: absolute;
    left: 0;
    width: 536px;
    top: 268px;
    text-align: center;
    font-size: 8.5px;
    font-weight: 600;
    text-transform: uppercase;
  }

  .back-brand {
    position: absolute;
    inset: 0;
    display: flex;
    flex-direction: column;
    align-items: center;
    justify-content: center;
    gap: 18px;
    font-weight: 700;
    font-size: 30px;
    letter-spacing: 0.06em;
    text-transform: uppercase;
    text-align: center;
    line-height: 1.2;
  }
  .back-brand .brand-mark { width: 40px; height: 40px; }
</style>
</head>
<body>
<main class="stage">
  <section class="card card--front" aria-label="Business card front">
    <svg class="edge-band" width="14" height="306" viewBox="0 0 14 306" aria-hidden="true">
      <polygon points="0,52 14,68 14,306 0,306" fill="var(--navy)"/>
    </svg>

    <div class="front-brand">
      <span class="brand-mark"></span>
      <span>Harrowmere<br>Holdings</span>
    </div>

    <div class="divider"></div>

    <div class="person">
      <p class="person-name">Dean Mollick</p>
      <p class="person-title">Director</p>
    </div>

    <div class="contact-list">
      <div class="contact-row">
        <span class="contact-label">Email</span>
        <span class="contact-value">harrowdean@quillnet.example</span>
      </div>
      <div class="contact-row">
        <span class="contact-label">Mobile</span>
        <span class="contact-value">0462 735 418</span>
      </div>
      <div class="contact-row">
        <span class="contact-label">Address</span>
        <span class="contact-value">4/312 Barnaby Parade<br>Halvercombe QX 7734, Australia</span>
      </div>
    </div>

    <p class="company-line">Harrowmere Holdings Pty Ltd</p>
  </section>

  <section class="card card--back" aria-label="Business card back">
    <div class="back-brand">
      <span class="brand-mark"></span>
      <span>Harrowmere<br>Holdings</span>
    </div>
  </section>
</main>
</body>
</html>
```